Quimby's Yard & Garden Center Business Card Update

I need an updated Business card design for my Lawn and Garden Center. We do Landscaping installs, Lawn Mowing, Snow Removal and also have a Garden Center Retail Division. I uploaded a few of our previous business cards to give an idea of what we are starting with. The main goal of this update is to simplify and modernize the business card, not all of the services that are on the previous cards has to be on the new one but I would still like to highlight our main services. There is also a sample of our logo that Can be used in the design.

Industry/Entity Type

Landscaping

Contact Information for Business Card

Morris Quimby
Morris@Quimbysyardandgarden.example
Business (555) 201-7784
Cell (555) 318-6092

Colors

Designer to choose colors to be used in the design.

Requirements
Must have
• Services Provided :
• Landscaping
• Lawn Maintenance
• Snow Removal
• Garden Center

```html
<!DOCTYPE html>
<html lang="en">
<head>
<meta charset="utf-8">
<title>Quimby's Yard & Garden Center – Business Card</title>
<link rel="stylesheet" href="https://fonts.googleapis.com/css2?family=Lato:wght@400;700&family=Montserrat:wght@400;700&display=swap">
<style>
  :root {
    --bg: #d6d6d9;
    --card: #ffffff;
    --green: #2b5a2a;
    --ink: #111111;
    --text: #3a3a3a;
    --rule: #b9b9b9;
    --icon: #4f6b4e;
  }
  * { margin: 0; padding: 0; box-sizing: border-box; }
  html, body { width: 1200px; height: 1200px; overflow: hidden; }
  body { background: var(--bg); position: relative; font-family: "Lato", sans-serif; }

  .card {
    position: absolute; left: 272px; width: 664px; height: 379px;
    background: var(--card); border: 2px solid var(--green);
  }
  .card--front { top: 171px; border-radius: 31px 0 31px 0; }
  .card--back { top: 631px; border-radius: 0 31px 0 31px; }

  .rule-v { position: absolute; width: 1px; background: var(--rule); }
  .rule-h { position: absolute; height: 1px; background: var(--rule); }

  .icon { position: absolute; left: 22px; width: 30px; height: 30px; }

  .name {
    position: absolute; left: 79px; top: 61px;
    font-family: "Montserrat", sans-serif; font-size: 26px; color: var(--ink);
    letter-spacing: 0.5px; line-height: 1;
  }
  .name strong { color: var(--green); font-weight: 700; }
  .role {
    position: absolute; left: 78px; top: 96px;
    font-family: "Montserrat", sans-serif; font-size: 15px; color: var(--ink);
  }
  .contact { position: absolute; left: 78px; font-size: 16.5px; color: var(--text); line-height: 19px; }
  .contact--email { font-family: "Montserrat", sans-serif; font-size: 15.5px; line-height: 18px; }

  .brand { position: absolute; text-align: center; color: var(--ink); font-family: "Lato", sans-serif; font-weight: 700; }
  .brand__dot { display: block; margin: 0 auto 14px; width: 70px; height: 70px; border-radius: 50%; background: var(--green); }
  .brand__name { display: block; font-size: 36px; line-height: 1; }
  .brand__sub { display: block; font-size: 13px; margin-top: 4px; }

  .services-title {
    position: absolute; left: 390px; top: 66px;
    font-weight: 700; font-size: 24px; color: var(--ink);
  }
  .services-title::after {
    content: ""; position: absolute; left: 3px; top: 32px; width: 38px;
    border-bottom: 2px dotted var(--ink);
  }
  .services { position: absolute; left: 390px; top: 126px; list-style: none; }
  .services li { font-size: 25px; color: var(--green); line-height: 35px; }

  .web {
    position: absolute; left: 22px; top: 336px;
    font-family: "Montserrat", sans-serif; font-size: 18px; color: var(--ink);
    display: flex; align-items: center; gap: 6px;
  }
</style>
</head>
<body>

<section class="card card--front">
  <div class="rule-v" style="left:65px; top:59px; height:262px;"></div>
  <div class="rule-h" style="left:22px; top:121px; width:270px;"></div>
  <div class="rule-h" style="left:22px; top:266px; width:270px;"></div>

  <svg class="icon" style="top:74px" viewBox="0 0 30 30" fill="none" stroke="var(--icon)" stroke-width="1.3" aria-hidden="true">
    <circle cx="15" cy="10" r="6"/><path d="M3 28c0-7 5-11 12-11s12 4 12 11z"/>
  </svg>
  <svg class="icon" style="top:136px" viewBox="0 0 30 30" fill="none" stroke="var(--icon)" stroke-width="1.3" aria-hidden="true">
    <path d="M2 10c0-4 6-6 13-6s13 2 13 6v2h-6V9H8v3H2z"/><path d="M7 14h16l3 12H4z"/><circle cx="15" cy="20" r="3"/>
  </svg>
  <svg class="icon" style="top:221px" viewBox="0 0 30 30" fill="none" stroke="var(--icon)" stroke-width="1.3" aria-hidden="true">
    <circle cx="15" cy="15" r="12"/><ellipse cx="15" cy="15" rx="5" ry="12"/><path d="M3 15h24M5 9h20M5 21h20"/>
  </svg>
  <svg class="icon" style="top:278px; height:34px" viewBox="0 0 30 34" fill="none" stroke="var(--icon)" stroke-width="1.3" aria-hidden="true">
    <path d="M15 32C8 22 4 17 4 12a11 11 0 0 1 22 0c0 5-4 10-11 20z"/><circle cx="15" cy="12" r="4"/>
  </svg>

  <h1 class="name"><strong>MORRIS</strong> QUIMBY</h1>
  <p class="role">OWNER</p>

  <p class="contact" style="top:130px">(555) 201-7784<br>(555) 318-6092</p>
  <p class="contact contact--email" style="top:215px">Morris@Quimbysyardandgarden.example<br>quimbysyardandgarden.example</p>
  <p class="contact" style="top:272px">4820 Meadow Lane Road,<br>Elmwood, Ohio 45999</p>

  <div class="brand" style="left:408px; top:110px; width:240px;">
    <span class="brand__dot"></span>
    <span class="brand__name">Quimby's</span>
    <span class="brand__sub">Yard &amp; Garden Center</span>
  </div>
</section>

<section class="card card--back">
  <div class="brand" style="left:33px; top:80px; width:240px;">
    <span class="brand__dot"></span>
    <span class="brand__name">Quimby's</span>
    <span class="brand__sub">Yard &amp; Garden Center</span>
  </div>

  <div class="rule-v" style="left:377px; top:58px; height:261px;"></div>
  <div class="rule-h" style="left:334px; top:121px; width:270px;"></div>
  <div class="rule-h" style="left:334px; top:266px; width:270px;"></div>

  <h2 class="services-title">We Do</h2>
  <ul class="services">
    <li>Landscaping installs</li>
    <li>Lawn Maintenance</li>
    <li>Snow Removal</li>
    <li>Garden Center</li>
  </ul>

  <p class="web">
    <svg width="12" height="12" viewBox="0 0 30 30" fill="none" stroke="var(--ink)" stroke-width="3" aria-hidden="true">
      <circle cx="15" cy="15" r="12"/><ellipse cx="15" cy="15" rx="5" ry="12"/><path d="M3 15h24"/>
    </svg>
    quimbysyardandgarden.example
  </p>
</section>

</body>
</html>
```